business stationery

have a gorgeous logo that needs to be incorporated on stationery. Was hoping to do something on letterhead that was a paper that looked like "bark" from a tree or something that resembled the "woods." Soft paper with some very basic natural elements. Same thing for business cards. Think American lakeside cabin. Organic. Natural. Calm and welcoming but clear to read and understand. Wanted to use alot of black.

Target Market(s)

buyers of Tobias Wrenfield home. Client that would have more than one home and in need of rare pieces and items to furnish an upmarket lakeside holiday cabin in the woods. Someone who treasures beautiful hand made items, organic foods and a real crackling fire but with money to burn in it!

Industry/Entity Type

Business

Requirements
Must have
• My logo
My business name
www.fernandcopper.example
Natural almost raw effect paper
My ABN: 62 307 514 928 (to be placed in small writing at the bottom of card/letterhead)
Nice to have
• The website will consist of a cabin door that you "open" with a creak sound effect and then you go "inside" to look at the various rooms to start shopping. Want to bring that element of texture and warmth into the stationary also.
Should not have
• Anything modern or hard to read items

```html
<!DOCTYPE html>
<html lang="en">
<head>
<meta charset="utf-8">
<title>Fern &amp; Copper — Stationery</title>
<link rel="stylesheet" href="https://fonts.googleapis.com/css2?family=Oswald:wght@400;600&display=swap">
<style>
  :root {
    --canvas: #ffffff;
    --kraft-light: #e9dcc0;
    --kraft-mid: #d9c29b;
    --kraft-edge: #c4a474;
    --bark-black: #151515;
    --bark-streak: #2a2a2a;
    --bark-shine: #3a3a3a;
    --ink: #1b1b1b;
    --ink-white: #f4f1ea;
    --ember-red: #7a1414;
    --card-edge: #111111;
  }

  * { margin: 0; padding: 0; box-sizing: border-box; }

  html, body {
    width: 960px;
    height: 1200px;
    overflow: hidden;
    background: var(--canvas);
    font-family: "Oswald", "Arial Narrow", sans-serif;
    color: var(--ink);
  }

  .stationery {
    position: relative;
    width: 960px;
    height: 1200px;
  }

  .kraft {
    background:
      radial-gradient(ellipse at 55% 55%, var(--kraft-light) 0%, var(--kraft-mid) 65%, var(--kraft-edge) 100%);
  }

  .bark {
    background:
      repeating-linear-gradient(90deg,
        var(--bark-black) 0px, var(--bark-black) 2px,
        var(--bark-streak) 3px, var(--bark-black) 5px,
        var(--bark-shine) 6px, var(--bark-black) 8px),
      var(--bark-black);
    background-blend-mode: normal;
  }

  /* Letterhead */
  .letterhead {
    position: absolute;
    left: 142px;
    top: 136px;
    width: 661px;
    height: 934px;
    overflow: hidden;
  }

  .letterhead__disc {
    position: absolute;
    left: -70px;
    top: -124px;
    width: 400px;
    height: 400px;
    border-radius: 50%;
  }

  .letterhead__brand {
    position: absolute;
    left: 22px;
    top: 92px;
    width: 248px;
    text-align: center;
    color: var(--ink-white);
  }

  .brand-name {
    display: flex;
    align-items: center;
    justify-content: center;
    gap: 10px;
    font-weight: 600;
    font-size: 38px;
    letter-spacing: 1px;
    line-height: 1;
    text-transform: uppercase;
  }

  .brand-dot {
    width: 12px;
    height: 12px;
    border-radius: 50%;
    background: var(--ink-white);
    flex: none;
  }

  .brand-byline {
    margin-top: 6px;
    text-align: right;
    font-size: 8px;
    letter-spacing: 0.5px;
    text-transform: uppercase;
  }

  .letterhead__footer {
    position: absolute;
    left: 0;
    top: 884px;
    width: 100%;
    font-size: 13px;
  }

  .letterhead__web {
    position: absolute;
    left: 188px;
    font-weight: 600;
    font-size: 15px;
  }

  .letterhead__abn {
    position: absolute;
    left: 388px;
    top: 2px;
    font-weight: 400;
    font-size: 12px;
  }

  /* Business card */
  .card {
    position: absolute;
    left: 617px;
    top: 630px;
    width: 280px;
    height: 160px;
    border-radius: 8px;
    border: 1px solid var(--card-edge);
    overflow: hidden;
  }

  .card__disc {
    position: absolute;
    left: -65px;
    top: -45px;
    width: 210px;
    height: 210px;
    border-radius: 50%;
  }

  .card__brand {
    position: absolute;
    left: 10px;
    top: 64px;
    width: 130px;
    color: var(--ink-white);
    text-align: center;
  }

  .card__brand .brand-name {
    font-size: 17px;
    gap: 5px;
    letter-spacing: 0.5px;
  }

  .card__brand .brand-dot {
    width: 6px;
    height: 6px;
  }

  .card__brand .brand-byline {
    font-size: 4px;
    margin-top: 3px;
  }

  .card__abn {
    position: absolute;
    left: 20px;
    top: 130px;
    font-size: 6px;
    color: var(--ink-white);
  }

  .card__contact {
    position: absolute;
    right: 20px;
    top: 112px;
    text-align: right;
  }

  .card__name {
    font-size: 11px;
    color: var(--ember-red);
    line-height: 1.2;
  }

  .card__web {
    font-size: 8px;
    color: var(--ink);
    line-height: 1.4;
  }
</style>
</head>
<body>
<main class="stationery">

  <section class="letterhead kraft" aria-label="Letterhead">
    <div class="letterhead__disc bark"></div>
    <div class="letterhead__brand">
      <div class="brand-name"><span class="brand-dot"></span>Fern &amp; Copper</div>
      <div class="brand-byline">by Maren Holloway</div>
    </div>
    <footer class="letterhead__footer">
      <span class="letterhead__web">www.fernandcopper.example</span>
      <span class="letterhead__abn">ABN: 62 307 514 928</span>
    </footer>
  </section>

  <section class="card kraft" aria-label="Business card">
    <div class="card__disc bark"></div>
    <div class="card__brand">
      <div class="brand-name"><span class="brand-dot"></span>Fern &amp; Copper</div>
      <div class="brand-byline">by Maren Holloway</div>
    </div>
    <div class="card__abn">ABN: 62 307 514 928</div>
    <div class="card__contact">
      <div class="card__name">Maren Holloway</div>
      <div class="card__web">www.fernandcopper.example</div>
    </div>
  </section>

</main>
</body>
</html>
```